Website design for Maple Nook Kidcare

I need a website designed for my daycare business, Maple Nook Kidcare, now that I have a new logo. My former website was ok but simple and I did not have a logo yet. It also was created by me using a template and was entirely pink. I loved the bright, happy feel of it but worried it might not appeal as much to potential clients who have sons. Therefore, I need a site which will appeal to both genders while still keeping the cheerful color scheme of my new logo, which has pinks, blue, green and cream.

Reason: Hello! I am still trying to download my new logo and am sorry it is taking me so long. Hopefully I will it posted by the end of today (US Eastern Standard Time). Thank you all very much for your patience!

Hello! I have finally managed to upload my new logo for you to use in designing my website. I'm sorry it took so long and greatly appreciate your time and creative efforts! I look forward to seeing what is submitted based on my logo design and its style/colors.

Many thanks!

Reason: As I've been traveling and posted my logo file late, I am extending my deadline. I am now back and can focus on providing more and better feedback. I appreciate your patience and submissions very much!

Reason: I need more time to provide feedback and make decisions.

Industry/Entity Type

Daycare

Colors
0192cd
33a6d7
86cae7
cadf82
fbf289
add136
e34197

```html
<!DOCTYPE html>
<html lang="en">
<head>
<meta charset="utf-8">
<title>Maple Nook Kidcare</title>
<link rel="stylesheet" href="https://fonts.googleapis.com/css2?family=Lato:wght@400;700&family=Open+Sans:wght@400;600;700&family=Short+Stack&display=swap">
<style>
:root{
  --pink:#e34197;
  --pink-soft:#ea86bb;
  --pink-pale:#fbe3ef;
  --green:#c9de86;
  --green-dark:#add136;
  --sky:#c6e5f0;
  --blue:#0192cd;
  --teal-ink:#2d5f6e;
  --ink:#3a3a3a;
  --grey:#6e6e6e;
  --cream:#fbf7e8;
  --white:#ffffff;
}
*{box-sizing:border-box;margin:0;padding:0}
html,body{width:920px;height:1200px;overflow:hidden;background:var(--white)}
body{position:relative;font-family:"Open Sans",sans-serif;color:var(--ink)}
.abs{position:absolute}

/* header */
.brand{left:147px;top:34px;width:200px;display:flex;align-items:center;gap:8px}
.brand-dot{width:14px;height:14px;border-radius:50%;background:var(--green-dark);flex:none}
.brand-name{font-family:"Lato",sans-serif;font-weight:700;font-size:25px;line-height:1.05;color:var(--pink)}
.contact-tag{left:652px;top:44px;width:138px;height:42px;background:var(--cream);border:1px solid #e3dcc4;border-radius:8px;
  box-shadow:0 1px 3px rgba(0,0,0,.15);font-family:"Short Stack",cursive;font-size:10px;line-height:14px;color:var(--pink);padding:6px 0 0 14px}

/* nav */
.main-nav{left:0;top:105px;width:920px;height:30px;background:var(--green);box-shadow:0 2px 3px rgba(0,0,0,.12)}
.main-nav ul{list-style:none;position:absolute;right:127px;top:0;display:flex;gap:14px;height:30px;align-items:center}
.main-nav a{color:var(--white);font-size:11px;font-weight:600;text-decoration:none}

/* hero */
.hero{left:0;top:135px;width:920px;height:333px;background:linear-gradient(135deg,#d9cfc2 0%,#bfb2a4 35%,#8b7f79 65%,#4c4a52 100%)}
.hero-caption{left:141px;top:321px;width:328px}
.hero-title{background:rgba(20,20,20,.88);color:var(--white);font-size:16px;padding:6px 10px;height:34px}
.hero-text{margin-top:3px;background:rgba(20,20,20,.8);color:#e8e8e8;font-size:8px;line-height:12px;padding:12px 10px 14px}
.hero-arrows{left:660px;top:424px;display:flex;gap:5px}

/* welcome */
.welcome-title{left:0;top:494px;width:920px;text-align:center;font-family:"Lato",sans-serif;font-size:17.5px;line-height:24px;color:var(--pink)}
.welcome-text{left:160px;top:565px;width:600px;text-align:center;font-size:9px;line-height:15px;color:var(--ink)}

/* features */
.features{left:0;top:642px;width:920px;height:187px;background:var(--sky)}
.feature{top:20px;width:200px;height:145px}
.feature + .feature{border-left:1px dotted #9cbfcc}
.feature h3{position:absolute;top:20px;font-size:13.5px;font-weight:600;color:var(--teal-ink)}
.feature-art{position:absolute;left:11px;top:47px;width:42px;height:42px;border-radius:6px;background:linear-gradient(135deg,#f5e9d9,#c9a9a0)}
.feature p{position:absolute;left:62px;top:44px;width:132px;font-size:8.8px;line-height:13px;color:var(--ink)}

/* news & testimonials */
.section-head{top:858px;display:flex;align-items:center;gap:8px;font-family:"Lato",sans-serif;font-size:17px;color:var(--pink)}
.section-rule{height:6px;background:repeating-linear-gradient(90deg,#c3dde9 0 1px,transparent 1px 3px)}
.news-text{left:138px;top:903px;width:200px;font-size:8.5px;line-height:13px;color:var(--grey)}
.testimonial-text{left:356px;top:903px;width:430px;font-size:8.5px;line-height:13px;color:var(--grey)}
.testimonial-arrows{left:716px;top:984px;display:flex;gap:4px}

/* footer */
.site-footer{left:0;top:1037px;width:920px;height:144px;background:var(--pink-soft)}
.footer-head{top:19px;font-family:"Lato",sans-serif;font-size:14px;color:var(--white)}
.footer-links{list-style:none;top:56px;font-size:8.5px;font-weight:600;line-height:14.5px}
.footer-links li::before{content:"›";color:#ffe87a;font-weight:700;margin-right:6px}
.footer-links a{color:var(--white);text-decoration:none}
.social{left:356px;top:56px;display:flex;gap:7px}
.social span{width:20px;height:20px;border-radius:3px;background:var(--white);border:2px solid #d5ecf5}
.baby-art{left:601px;top:60px;width:52px;height:60px;border-radius:26px;background:linear-gradient(180deg,#fde0c6,#f3b58c)}
.address{left:661px;top:61px;font-family:"Short Stack",cursive;font-size:9.5px;line-height:13px;color:var(--white)}
.copyright{left:0;top:1181px;width:920px;height:19px;background:var(--pink-pale);text-align:right;padding-right:127px;font-size:7px;line-height:19px;color:var(--ink)}
</style>
</head>
<body>

<header>
  <div class="abs brand">
    <span class="brand-dot"></span>
    <span class="brand-name">Maple Nook<br>Kidcare</span>
  </div>
  <div class="abs contact-tag">(555) 014-3920<br>hello@maplenookkids.com</div>
</header>

<nav class="abs main-nav">
  <ul>
    <li><a href="#">Home</a></li>
    <li><a href="#">About us</a></li>
    <li><a href="#">Services</a></li>
    <li><a href="#">Hour &amp; Fee</a></li>
    <li><a href="#">Policies</a></li>
    <li><a href="#">Contact us</a></li>
    <li><a href="#">Photoes</a></li>
    <li><a href="#">Testimonials</a></li>
  </ul>
</nav>

<section class="abs hero" role="img" aria-label="Photo of toddlers and caregivers playing together on a playroom floor"></section>
<div class="abs hero-caption">
  <div class="hero-title">Sed ut perspiciatis unde omnis iste</div>
  <div class="hero-text">Sed ut perspiciatis unde omnis iste natus error sit voluptatem accusantium doloremque laudantium, totam rem aperiam, eaque ipsa quae ab illo inventore veritatis et quasi architecto beatae vitae dicta sunt explicabo.</div>
</div>
<div class="abs hero-arrows">
  <svg width="24" height="24" viewBox="0 0 24 24"><circle cx="12" cy="12" r="11" fill="#fff"/><path d="M14 7l-5 5 5 5" fill="none" stroke="#0192cd" stroke-width="2.4" stroke-linecap="round" stroke-linejoin="round"/></svg>
  <svg width="24" height="24" viewBox="0 0 24 24"><circle cx="12" cy="12" r="11" fill="#fff"/><path d="M10 7l5 5-5 5" fill="none" stroke="#0192cd" stroke-width="2.4" stroke-linecap="round" stroke-linejoin="round"/></svg>
</div>

<h1 class="abs welcome-title" style="font-weight:400">Welcome to Maple Nook Kidcare, a playspace<br>where children can play, create, and imagine!</h1>
<p class="abs welcome-text">Welcome to Maple Nook Kidcare, a licensed Group Family Day Care, located in Brookvale's leafy Linden Hill district. We are located on a pretty, tree-lined block on Linden Row, between Oak and Birch Lanes. We are a few blocks from the Brookvale train station and the Linden Row bus route, and we offer flexible hourly childcare, making it as easy as possible for busy parents on the go to arrange their children's care.</p>

<section class="abs features">
  <div class="abs feature" style="left:131px">
    <h3 style="left:61px">Learning</h3>
    <div class="feature-art" role="img" aria-label="Illustration of a stack of books"></div>
    <p>We develop age-appropriate activities that introduce and strengthen academic and social skills.</p>
  </div>
  <div class="abs feature" style="left:347px">
    <h3 style="left:62px">Creativity</h3>
    <div class="feature-art" role="img" aria-label="Illustration of a cup of paint brushes"></div>
    <p>We offer children a wide range of creative opportunities including art projects, toddler yoga lessons, afternoon tea parties, dress up play, and a large selection of books.</p>
  </div>
  <div class="abs feature" style="left:566px">
    <h3 style="left:72px">Sharing</h3>
    <div class="feature-art" role="img" aria-label="Illustration of a picnic basket"></div>
    <p style="left:74px">We strive to include enrichment activities that extend your child's understanding of the world and their role in it.</p>
  </div>
</section>

<h2 class="abs section-head" style="left:134px;font-weight:400">News <span class="section-rule" style="width:160px"></span></h2>
<h2 class="abs section-head" style="left:362px;font-weight:400">Testimonials <span class="section-rule" style="width:324px"></span></h2>
<p class="abs news-text">We are thrilled to have found a new cheerful space with a private backyard! It's large, sunny, and filled with outdoor play equipment such as a toddler slide, sand/water activity table, and lots of toys! Please stay tuned for updates on our program and services as we say goodbye to Winter and hello to Spring!</p>
<p class="abs testimonial-text">Sed ut perspiciatis unde omnis iste natus error sit voluptatem accusantium doloremque laudantium, totam rem aperiam, eaque ipsa quae ab illo inventore veritatis et quasi architecto beatae vitae dicta sunt explicabo. Nemo enim ipsam voluptatem quia voluptas sit aspernatur aut odit aut fugit, sed quia consequuntur magni dolores eos qui ratione voluptatem sequi nesciunt.</p>
<div class="abs testimonial-arrows">
  <svg width="24" height="24" viewBox="0 0 24 24"><circle cx="12" cy="12" r="12" fill="#ea86bb"/><path d="M14 7l-5 5 5 5" fill="none" stroke="#fff" stroke-width="2.4" stroke-linecap="round" stroke-linejoin="round"/></svg>
  <svg width="24" height="24" viewBox="0 0 24 24"><circle cx="12" cy="12" r="12" fill="#ea86bb"/><path d="M10 7l5 5-5 5" fill="none" stroke="#fff" stroke-width="2.4" stroke-linecap="round" stroke-linejoin="round"/></svg>
</div>

<footer class="abs site-footer">
  <h4 class="abs footer-head" style="left:131px;font-weight:400">Navigation</h4>
  <ul class="abs footer-links" style="left:131px">
    <li><a href="#">Home</a></li>
    <li><a href="#">About us</a></li>
    <li><a href="#">Services</a></li>
    <li><a href="#">Hour &amp; Fee</a></li>
  </ul>
  <ul class="abs footer-links" style="left:238px">
    <li><a href="#">Policies</a></li>
    <li><a href="#">Contact us</a></li>
    <li><a href="#">Photos</a></li>
    <li><a href="#">Testimonials</a></li>
  </ul>
  <h4 class="abs footer-head" style="left:358px;font-weight:400">Get social with us</h4>
  <div class="abs social" aria-label="Social links">
    <span></span><span></span><span></span><span></span>
  </div>
  <h4 class="abs footer-head" style="left:578px;font-weight:400">Our Location</h4>
  <div class="abs baby-art" role="img" aria-label="Illustration of a smiling baby"></div>
  <address class="abs address" style="font-style:normal">Dana Whitfield<br>118 Linden Row<br>Brookvale, NY 10990<br>Phone: (555) 014-3920<br>Email: hello@maplenookkids.com</address>
</footer>
<div class="abs copyright">COPYRIGHT 2014, ALL RIGHT RESERVED MAPLE NOOK KIDCARE</div>

</body>
</html>
```